I need a label created within the following dimensions below:

Label/Screen Printable Area:

Width 6.742”

Height 5.731”

The bottle dimensions are 7.175 (H) x 2.146 (D)

This is for 2 seperate labels.  One label for my hair Shampoo and another label for my hair Conditioner.

Requirements
Must have
• Front of Shampoo bottle:

Verdant Morning Roots logo

Product name (shampoo – Nourishing & Hydrating)

Bottle volume: 12 fl. Oz. (355ml)

Side of bottle:

"Verdant Strengthening with pure oil Essentials"

Back of bottle:

Verdant Morning Roots Shampoo is a blend of heavenly, ingredients from Mother Earth that nourish, protect and beautify your hair and extend the life of color. Our Products are Sulfate-Free, Paraben-Free, Contain No Artificial Colors and are Not Tested on Animals.

Distributed By and/or Get more information: (Distributed By: Morning Roots, Elmbrook, IL 60999/ Get more information and connect with Morning Roots at www.verdantmorningroots.com)

Ingredients: (I’ve included the ingredients listings below for quick copying to your art file)

DESCRIPTION: Morning Roots Shampoo

How to/ Directions for use: (Apply to wet hair. Massage into a rich lather. Rinse. Repeat if necessary.)

INGREDIENTS: Purified Water, Sodium Methyl 2-Sulfolaurate & Disodium 2-Sulfolaurate & Cocamidopropyl Betaine, Cetrimonium Chloride, Distearyl Phthalic Acid Amide, Simmondsia Chinensis (Organic Jojoba Seed) Oil, Butyrospermum Parkii (Organic Shea Butter) Fruit, Aloe Barbadensis Leaf Juice (Organic Aloe Vera Gel), Hydrolyzed Quinoa (Protein), Dimethicone, Fragrance (Apple, Pear, White Grape), Gluconolactone & Sodium Benzoate (Natural Preservative), Panthenol (Vitamin B-5), Citric Acid, Tocopherol (Vitamin E).

Front of conditioner bottle:

Product name: (Conditioner Shampoo - luxurious volume conditioner)

Side of bottle:

Back of bottle:

DESCRIPTION: Morning Roots Restructurant Conditioner

How to/ Directions for use: (Apply to wet hair. Massage into hair and sit for 5 minutes. For a deep conditoner treatment apply to hair and sit under the hair dryer for 20-30 minutes, Repeat if necessary; then rinse and style as usual).

INGREDIENTS: Purified Water, Behentrimonium Methosulfate (Modified Rapseed Oil), Cetearyl Alcohol, Cetyl Alcohol, Cetrimonium Chloride, Cyclopentasiloxane and Dimethicone, Caprylic/Capric Triglyceride, Extracts of Foeniculum Vulgare (Fennel Seed) and Helianthus Annuus (Sunflower Seed), Simmondsia Chinensis (Jojoba Seed) Oil, Olea Europaea (Olive Fruit) Oil, Fragrance, Mentha Piperita (Peppermint) Oil, Mentha (Menthol), Aloe Barbadensis Leaf Juice (Organic Aloe Vera Gel), Hydrolyzed Hair Keratin, Butyrospermum Parkii (Organic Shea Butter) Fruit, Sodium Benzoate (Natural Preservative) and Potassium Sorbate, Rosmarinus Officinalis (Rosemary) Oil, Lavandula Officinalis (Lavender) Oil, Panthenol (Vitamin B-5), Tocopherol (Vitamin E), Guar Hydroxypropyltrimonium Chloride, Citric Acid.

Width 6.742”

Height 5.731”

Should not have
• No other colors then what my logo colors currently are.

```html
<!DOCTYPE html>
<html lang="en">
<head>
<meta charset="utf-8">
<title>Verdant Morning Roots – Restructuring Conditioner Label</title>
<link rel="stylesheet" href="https://fonts.googleapis.com/css2?family=Open+Sans:wght@400;600;700&display=swap">
<style>
  :root {
    --gold: #a87b2c;
    --gold-dark: #8c6420;
    --green: #1d5a3a;
    --cream: #e9e1d3;
    --label-white: #ffffff;
    --page: #f4f4f2;
    --leaf-light: #a6d64a;
    --leaf-dark: #5c9a1f;
  }
  * { box-sizing: border-box; margin: 0; padding: 0; }
  html, body { width: 1200px; height: 1020px; overflow: hidden; }
  body {
    background: var(--page);
    font-family: "Open Sans", Arial, sans-serif;
    position: relative;
  }
  .panel {
    position: absolute;
    background: var(--label-white);
    overflow: hidden;
    box-shadow: 0 0 0 1px #dcdcd8;
  }
  .panel__swoosh { position: absolute; inset: 0; width: 100%; height: 100%; }

  /* Front */
  .front { left: 70px; top: 250px; width: 345px; height: 660px; }
  .brand {
    position: absolute; left: 0; right: 0; top: 90px;
    text-align: center;
  }
  .brand__mark {
    display: block; width: 26px; height: 26px; border-radius: 50%;
    background: var(--gold); margin: 0 auto 14px;
  }
  .brand__name {
    font-weight: 700; font-size: 29px; line-height: 1.15; color: var(--green);
  }
  .leaf-art {
    position: absolute; left: 80px; top: 300px; width: 185px; height: 110px;
    border-radius: 50% 50% 40% 40%;
    background: radial-gradient(ellipse at 50% 40%, var(--leaf-light), var(--leaf-dark));
  }
  .product-name {
    position: absolute; left: 22px; top: 440px; width: 302px; height: 80px;
    background: var(--gold); color: #fff;
    display: flex; flex-direction: column; justify-content: center; align-items: center;
    font-weight: 600; font-size: 21px; line-height: 1.3;
  }
  .volume {
    position: absolute; right: 38px; bottom: 22px;
    color: var(--gold); font-weight: 600; font-size: 19px;
  }

  /* Side */
  .side { left: 560px; top: 250px; width: 60px; height: 660px; }
  .side__tagline {
    position: absolute; left: 50%; top: 50%;
    transform: translate(-50%, -50%) rotate(-90deg);
    white-space: nowrap;
    color: var(--gold); font-weight: 700; font-size: 22.5px;
  }

  /* Back */
  .back { left: 760px; top: 250px; width: 390px; height: 660px; }
  .back__copy {
    position: absolute; left: 66px; right: 14px; top: 52px;
    color: var(--gold); font-weight: 700; font-size: 12.6px; line-height: 1.3;
    text-align: justify;
  }
  .back__copy p { margin-bottom: 17px; }
  .distributor {
    position: absolute; left: 66px; right: 14px; bottom: 28px; height: 56px;
    background: var(--gold); color: #fff;
    font-weight: 700; font-size: 7.4px; line-height: 1.9;
    padding: 7px 8px;
  }
</style>
</head>
<body>

<section class="panel front" aria-label="Front label">
  <svg class="panel__swoosh" viewBox="0 0 345 660" preserveAspectRatio="none" aria-hidden="true">
    <path d="M345 0 C260 60 250 190 345 300 Z" fill="var(--cream)"/>
    <path d="M0 360 C120 300 310 360 345 450 L345 660 L110 660 C40 560 10 450 0 430 Z" fill="var(--cream)"/>
    <path d="M0 480 C40 600 120 650 200 660 L0 660 Z" fill="var(--label-white)"/>
  </svg>
  <div class="brand">
    <span class="brand__mark"></span>
    <div class="brand__name">Verdant Morning<br>Roots</div>
  </div>
  <div class="leaf-art" role="img" aria-label="Green leaves illustration"></div>
  <div class="product-name">
    <span>Restructuring Conditioner</span>
    <span>Luxurious Volume</span>
  </div>
  <div class="volume">12 fl. Oz. (355ml)</div>
</section>

<section class="panel side" aria-label="Side label">
  <div class="side__tagline">Verdant Strengthening with pure oil Essentials</div>
</section>

<section class="panel back" aria-label="Back label">
  <svg class="panel__swoosh" viewBox="0 0 390 660" preserveAspectRatio="none" aria-hidden="true">
    <path d="M0 20 C40 140 70 300 60 660 L0 660 Z" fill="var(--cream)"/>
    <path d="M390 70 C300 110 280 250 390 350 Z" fill="var(--cream)"/>
  </svg>
  <div class="back__copy">
    <p>Verdant Morning Roots Shampoo is a blend of heavenly, ingredients from Mother Earth that nourish, protect and beautify your hair and extend the life of color. Our Products are Sulfate-Free, Paraben-Free, Contain No Artificial Colors and are Not Tested on Animals.</p>
    <p>How to/ Directions for use: (Apply to wet hair. Massage into hair and sit for 5 minutes. For a deep conditoner treatment apply to hair and sit under the hair dryer for 20-30 minutes, Repeat if necessary; then rinse and style as usual).</p>
    <p>INGREDIENTS: Purified Water, Behentrimonium Methosulfate (Modified Rapseed Oil), Cetearyl Alcohol, Cetyl Alcohol, Cetrimonium Chloride, Cyclopentasiloxane and Dimethicone, Caprylic/Capric Triglyceride, Extracts of Foeniculum Vulgare (Fennel Seed) and Helianthus Annuus (Sunflower Seed), Simmondsia Chinensis (Jojoba Seed) Oil, Olea Europaea (Olive Fruit) Oil, Fragrance, Mentha Piperita (Peppermint) Oil, Mentha (Menthol), Aloe Barbadensis Leaf Juice (Organic Aloe Vera Gel), Hydrolyzed Hair Keratin, Butyrospermum Parkii (Organic Shea Butter) Fruit, Sodium Benzoate (Natural Preservative) and Potassium Sorbate, Rosmarinus Officinalis (Rosemary) Oil, Lavandula Officinalis (Lavender) Oil, Panthenol (Vitamin B-5), Tocopherol (Vitamin E), Guar Hydroxypropyltrimonium Chloride, Citric Acid.</p>
  </div>
  <div class="distributor">
    Distributed By and/or Get more information: (Distributed By: Morning Roots, Elmbrook, IL 60999/ Get more information and connect with Morning Roots at www.verdantmorningroots.com)
  </div>
</section>

</body>
</html>
```